Thabeng Academy one-page profile

I need to develop a professionally designed "one-pager" for a new independent school opening in the Alexandra Township in South Africa in 2015. Alexandra is one of the poorest communities in South Africa and our aim is to bring a university preparatory education to this community. The school will open with kindergarten students and will expand each year until we reach grade 12. I would like for the file to be in a format that I can easily edit in the event that the information that I provide in the attachment changes or should I choose to utilize the format for an additional flyer.

The document needs to be designed as an A4 paper sized document as opposed to the standard size used in the United States.

I like the format of the following document:
http://www.brolvane.org/pdfs/11.30.2012%20RTDF%20Tutoring%20One%20Pager.pdf
http://www.pelquorin.com/images/150_Teacher_recruitment_flyer.jpg
http://dunrovel.org/2013/01/18/ZEBN%2520QTAF%2520Lottery%2520Information_English%2520Flyer%5B1%5D.jpg
Updates

I edited the attached Thabeng Academy one page profile by altering it slightly and cutting out some unnecessary wording.  Please view to make changes.

Target Market(s)

The target market for this piece are potential funders and partners.

Industry/Entity Type

University

Requirements
Must have
• The design must use the Thabeng Academy colors and fonts as outlined in the branding guide. The design must look professional and must give the impression of a stellar private school.
Should not have
• Clip art

```html
<!DOCTYPE html>
<html lang="en">
<head>
<meta charset="utf-8">
<title>Thabeng Academy – One-Page Profile</title>
<link rel="stylesheet" href="https://fonts.googleapis.com/css2?family=Crimson+Text:wght@400;600&family=Open+Sans:wght@700&display=swap">
<style>
  :root {
    --backdrop: #000000;
    --paper: #ffffff;
    --brand-blue: #2f76b8;
    --brand-blue-text: #3a7bc0;
    --brand-green: #8dc63f;
    --brand-orange: #f39a1e;
    --brand-yellow: #ffed00;
    --brand-magenta: #a0186c;
    --tile-blue: #2b7bbd;
    --ink: #1c1c1c;
    --ink-soft: #333333;
    --on-colour: #ffffff;
  }
  * { box-sizing: border-box; margin: 0; padding: 0; }
  html, body { width: 917px; height: 1200px; overflow: hidden; background: var(--backdrop); }
  body { position: relative; font-family: "Crimson Text", Georgia, serif; }

  .profile {
    position: absolute; left: 87px; top: 75px;
    width: 742px; height: 1049px;
    background: var(--paper);
    display: grid;
    grid-template-columns: 274px 468px;
    grid-template-rows: 445px 280px 324px;
  }

  /* ---------- masthead column ---------- */
  .masthead { grid-column: 1; grid-row: 1; display: flex; flex-direction: column; }
  .brand {
    height: 147px; display: flex; align-items: center; justify-content: center;
    background: var(--paper);
  }
  .brand-row { display: flex; align-items: center; gap: 10px; white-space: nowrap; }
  .brand-dot { width: 20px; height: 20px; border-radius: 50%; background: var(--brand-blue); flex: none; }
  .brand-name {
    font-family: "Crimson Text", Georgia, serif; font-weight: 600;
    font-size: 23px; color: var(--brand-blue); letter-spacing: 0.4px; line-height: 1;
  }
  .web-band {
    height: 27px; background: var(--brand-yellow);
    font-size: 19px; color: var(--ink); padding-left: 24px; line-height: 27px;
  }
  .photo-toddler {
    height: 255px;
    background: linear-gradient(135deg, #e9c9a0 0%, #f0a24a 30%, #7ab6de 60%, #c8d9e6 100%);
  }
  .accent-strip { height: 16px; background: var(--brand-orange); }

  .photo-reader {
    grid-column: 2; grid-row: 1;
    background: radial-gradient(ellipse at 55% 45%, #f3ece4 0%, #e4ecf4 45%, #ffffff 100%);
  }

  /* ---------- shared headings ---------- */
  .sidebar h2, .model h2, .main h2 {
    font-family: "Crimson Text", Georgia, serif; font-weight: 400;
    font-size: 15.5px; letter-spacing: 0.3px; text-transform: uppercase; line-height: 1.1;
  }

  /* ---------- left blue column ---------- */
  .sidebar {
    grid-column: 1; grid-row: 2 / span 2;
    background: var(--brand-blue); color: var(--on-colour);
    padding: 14px 18px 0 24px;
    font-size: 11.4px; line-height: 1.2;
  }
  .sidebar h2 { margin-top: 12px; }
  .sidebar h2:first-child { margin-top: 0; }
  .sidebar p { margin-top: 1px; }
  .sidebar p + p { margin-top: 10px; }

  /* ---------- green model panel ---------- */
  .model {
    grid-column: 2; grid-row: 2;
    background: var(--brand-green); color: var(--ink);
    padding: 10px 16px 0 15px;
    font-size: 11.4px; line-height: 1.2;
  }
  .model h2 { margin-top: 12px; }
  .feature-columns {
    display: grid; grid-template-columns: 205px 1fr; column-gap: 14px; margin-top: 9px;
  }
  .feature-list { list-style: none; display: flex; flex-direction: column; gap: 2px; }
  .feature-list li { position: relative; padding-left: 19px; }
  .feature-list li::before {
    content: ""; position: absolute; left: 5px; top: 5px;
    width: 4px; height: 4px; border-radius: 50%; background: var(--ink);
  }

  /* ---------- white lower panel ---------- */
  .main {
    grid-column: 2; grid-row: 3;
    padding: 11px 16px 0 15px;
    font-size: 11.4px; line-height: 1.2; color: var(--ink-soft);
  }
  .main h2 { color: var(--brand-blue-text); }
  .components { display: grid; grid-template-columns: 128px 1fr; margin-top: 8px; }
  .components-intro { padding-right: 10px; margin-top: 4px; }
  .tile-grid {
    display: grid; grid-template-columns: 139px 139px; grid-auto-rows: 85px;
    column-gap: 10px; row-gap: 7px; margin-left: 10px;
  }
  .tile { display: flex; flex-direction: column; align-items: center; color: var(--on-colour); }
  .tile-label {
    font-family: "Open Sans", Arial, sans-serif; font-weight: 700;
    font-size: 9.4px; line-height: 1.15; text-align: center; padding-top: 2px; height: 26px;
  }
  .tile svg { width: 46px; height: 46px; margin-top: 2px; }
  .tile--justice { background: var(--brand-orange); }
  .tile--planning { background: var(--tile-blue); }
  .tile--literacy { background: var(--brand-magenta); }
  .tile--data { background: var(--brand-green); }
  .questions { margin-top: 20px; }
  .questions p { margin-top: 4px; font-size: 11.6px; }
  .contact { font-weight: 600; font-size: 13px; color: var(--ink); }
</style>
</head>
<body>
<article class="profile">

  <header class="masthead">
    <div class="brand">
      <div class="brand-row">
        <span class="brand-dot"></span>
        <span class="brand-name">THABENG ACADEMY</span>
      </div>
    </div>
    <div class="web-band">www.masedifoundation.org</div>
    <div class="photo-toddler" role="img" aria-label="Photo of a toddler reading a picture book beside colourful chairs"></div>
    <div class="accent-strip"></div>
  </header>

  <div class="photo-reader" role="img" aria-label="Photo of a smiling young boy reading a large book"></div>

  <aside class="sidebar">
    <h2>Who are we</h2>
    <p>Thabeng Academy will open its doors in January 2015 as the first Grade R- 12 university preparatory school in Alexandra. Admission to Thabeng Academy ison a first come, first serve basis and the schoolwill serve Grade R students in 2015 and will add a new grade each year.</p>
    <p>Thabeng Academy is a proud member of The Open Horizon Network of Schools, an organization, founded in the United States, committed to building a global network of transformational breakthrough schools.</p>

    <h2>Our community</h2>
    <p>Alexandrais a historic area located in the Gauteng Province in South Africa with several notable leaders residing in Alexandra at some point in their journey, including President Sipho Dlamini and former First Lady Thandi Mokoena. Alexandra is a community full of promise but is considered one of the most economically disenfranchised urban communities in the country. The average household income in Alexandra is under R5000.00 per month and an estimated population of 500,000 people live on 1 square mile of land.</p>

    <h2>Our school leader</h2>
    <p>Naledi Jefferson-Mokoena is passionate about education and social justice and has been a contributing writer for Learning Southern Africa and Reimagining Classrooms and in 2012 Naledi gave a IdeaX talk on the importance of an education steeped in social justice. Naledi is excited about the opportunity to learn and serve the Alexandra Township and is one of the organizers for IdeaXAlexandra. In 2013,</p>
  </aside>

  <section class="model">
    <p>Naledi completed the highly selective Ridgeway Global Fellowship in the United States which is a specialized programmethat prepares fellows to found and lead high performing schools in underserved communities.Prior to establishing the Thabeng Academy, Naledi taught middle school humanities for seven years and worked as an education programme coordinator. Naledi holds an MS Degree in Education Policy from the University of Lakemont, where she was an Advanced Opportunity Fellow and a BAin education from Harlow College.</p>
    <h2>Our model</h2>
    <p>Thabeng Academy has several unique features aimed to put all students on the path to university:</p>
    <div class="feature-columns">
      <ul class="feature-list">
        <li>University preparatory curriculum and learning environment</li>
        <li>Highly qualified, caring, and passionate educators and staff</li>
        <li>Extended School Day</li>
      </ul>
      <ul class="feature-list">
        <li>Dual Language Programme (English and Zulu0</li>
        <li>Creative Arts and movement classes</li>
        <li>Technology Integration across subject areas</li>
        <li>Extra-murals built into the school day</li>
      </ul>
    </div>
  </section>

  <section class="main">
    <h2>Core components</h2>
    <div class="components">
      <p class="components-intro">At Thabeng Academy, we have outlined four core components that will be prioritized, witheach area providing an avenue for achieving our mission of ensuring that all students are prepared with the academic and character skills that they need to be successful in university.</p>
      <div class="tile-grid">
        <div class="tile tile--justice">
          <span class="tile-label">Social Justice Foundation</span>
          <svg viewBox="0 0 48 48" aria-hidden="true" fill="none" stroke="#111" stroke-width="2.4" stroke-linecap="round">
            <line x1="24" y1="5" x2="24" y2="41"/><line x1="9" y1="11" x2="39" y2="11"/>
            <line x1="15" y1="43" x2="33" y2="43"/>
            <path d="M9 11 L3 26 H15 Z"/><path d="M39 11 L33 26 H45 Z"/>
            <path d="M3 26 Q9 32 15 26" fill="#111"/><path d="M33 26 Q39 32 45 26" fill="#111"/>
          </svg>
        </div>
        <div class="tile tile--planning">
          <span class="tile-label">Standards Based Unit and Lesson Planning</span>
          <svg viewBox="0 0 48 48" aria-hidden="true">
            <path d="M34 5 L43 14 L17 40 L6 43 L9 32 Z" fill="#111"/>
            <line x1="30" y1="9" x2="39" y2="18" stroke="#2b7bbd" stroke-width="2.4"/>
          </svg>
        </div>
        <div class="tile tile--literacy">
          <span class="tile-label">Literacy Focus</span>
          <svg viewBox="0 0 48 48" aria-hidden="true" fill="none" stroke="#111" stroke-width="3" stroke-linejoin="round">
            <path d="M24 12 C17 7 9 7 4 9 V40 C9 38 17 38 24 42 Z"/>
            <path d="M24 12 C31 7 39 7 44 9 V40 C39 38 31 38 24 42 Z"/>
          </svg>
        </div>
        <div class="tile tile--data">
          <span class="tile-label">Data Driven Instruction</span>
          <svg viewBox="0 0 48 48" aria-hidden="true" fill="#111">
            <path d="M5 6 V43 H44" fill="none" stroke="#111" stroke-width="3"/>
            <rect x="11" y="30" width="5" height="11"/><rect x="19" y="24" width="5" height="17"/>
            <rect x="27" y="27" width="5" height="14"/><rect x="35" y="18" width="5" height="23"/>
            <path d="M10 24 L20 15 L28 20 L41 8" fill="none" stroke="#111" stroke-width="2.4"/>
          </svg>
        </div>
      </div>
    </div>

    <div class="questions">
      <h2>Questions</h2>
      <p>If you have questions, please contact a member of our team at <span class="contact">+27 71-555-0148</span> or by email at <span class="contact">info@masedifoundation.org.</span></p>
    </div>
  </section>

</article>
</body>
</html>
```